Serene Spiritual Website Wanted for World Wide Organisation

We need a serene, clean web design for our organisation that works around the world.

What We Do
We aim to bring life into synergy across the world. We inspire, motivate, synchronise, and harmonise. We work with energy which is essential to all of life (environmental, human & animal). Our website must depict the spiritual element of being innately natural and reflect animism.

We have included a PDF attachment with details of the structure, navigation, and some websites for ideas/reference. The logo is also attached.
Updates

Target Market(s)

Anyone over 18yrs looking for answers to life's big questions or looking to develop themselves

Industry/Entity Type

Spiritual/wellbeing/Self Development

Number of Pages Required

5+ page

Requirements
Must have
• It must be serene and natural looking, it must incorporate the logo.
Nice to have
• We have included a Powerpoint document which may help you understand what we need, it is just an idea for structure and style, it is not set in stone so feel free to be as creative as you like!
Should not have
• Not clinical.

```html
<!DOCTYPE html>
<html lang="en">
<head>
<meta charset="utf-8">
<title>Harmonia</title>
<link href="https://fonts.googleapis.com/css2?family=Playfair+Display:wght@400&family=Nunito+Sans:wght@400;600;700&display=swap" rel="stylesheet">
<style>
:root{
  --navy:#3f4069;
  --gold:#ecd98a;
  --gold-text:#e8cf6a;
  --ink:#2b2b33;
  --white:#ffffff;
  --dark:#2a2b30;
  --footer-text:#444450;
}
*{margin:0;padding:0;box-sizing:border-box}
html,body{width:1122px;height:1200px;overflow:hidden}
body{position:relative;font-family:"Nunito Sans",sans-serif;background:var(--white);color:var(--ink)}
.site-header{position:absolute;left:0;top:0;width:1122px;height:79px;background:var(--navy)}
.brand{position:absolute;left:238px;top:28px;display:flex;align-items:center;gap:7px;color:var(--gold-text);font-weight:700;font-size:17px;letter-spacing:1px;text-transform:lowercase}
.brand-dot{width:16px;height:16px;border-radius:50%;background:var(--gold-text)}
.main-nav{position:absolute;top:34px;left:0;width:100%}
.main-nav a{position:absolute;color:var(--white);text-decoration:none;font-size:11px;font-weight:600}
.hero{position:absolute;left:0;top:79px;width:1122px;height:416px;
  background:linear-gradient(180deg,#b79a7e 0%,#a98560 30%,#8f6636 55%,#a6653a 75%,#7a4526 100%)}
.hero-title{position:absolute;left:227px;top:138px;font-family:"Playfair Display",serif;font-weight:400;font-size:35px;line-height:39px;color:var(--white);letter-spacing:-0.5px}
.hero-tagline{position:absolute;left:227px;top:226px;width:262px;height:26px;border-radius:5px;background:var(--gold);color:var(--navy);font-size:10.5px;font-weight:700;line-height:26px;text-align:center}
.events{position:absolute;left:0;top:495px;width:1122px;height:575px;
  background:linear-gradient(180deg,#3b3d44 0%,#2f3235 45%,#2c3129 80%,#2d3027 100%)}
.events-band{position:absolute;left:0;top:1060px;width:1122px;height:10px;background:var(--dark)}
.events-title{position:absolute;left:0;width:1116px;top:102px;text-align:center;color:var(--white);font-size:23px;font-weight:600;letter-spacing:.5px}
.event-card{position:absolute;top:161px;width:153px;height:232px;background:var(--white);text-align:center}
.event-photo{width:103px;height:103px;border-radius:50%;margin:21px auto 0}
.event-name{font-family:"Playfair Display",serif;font-size:13px;line-height:18px;color:#3a3a3a;margin-top:11px}
.event-date{font-size:7px;font-weight:700;color:#444;margin-top:6px}
.btn-events{position:absolute;left:505px;top:425px;width:112px;height:29px;border-radius:4px;background:var(--gold);color:var(--ink);font-size:9.5px;font-weight:700;line-height:29px;text-align:center}
.site-footer{position:absolute;left:0;top:1070px;width:1122px;height:130px;background:var(--white)}
.contact,.legal{position:absolute;font-size:11px;line-height:17px;color:var(--footer-text);font-weight:600}
.contact{left:242px;top:55px}
.legal{left:711px;top:52px}
.divider{position:absolute;top:38px;width:2px;height:64px;background:#222}
.social{position:absolute;top:64px;display:flex;gap:17px;left:505px}
.social span{width:14px;height:14px;border-radius:50%;background:#1f1f1f}
</style>
</head>
<body>
<header class="site-header">
  <div class="brand"><span class="brand-dot"></span>Harmonia</div>
  <nav class="main-nav">
    <a style="left:629px">About</a>
    <a style="left:676px">Events</a>
    <a style="left:725px">Synergise</a>
    <a style="left:789px">Wisdom</a>
    <a style="left:846px">Shop</a>
  </nav>
</header>

<section class="hero" role="img" aria-label="Hiker standing on red sandstone cliffs overlooking a green canyon valley at sunset">
  <h1 class="hero-title">We aim to bring life into<br>synergy across the world.</h1>
  <div class="hero-tagline">We inspire, motivate, synchronise, and harmonise.</div>
</section>

<section class="events" role="img" aria-label="Dim forest of tall pines beneath a granite cliff">
  <h2 class="events-title">Events</h2>
  <article class="event-card" style="left:227px">
    <div class="event-photo" role="img" aria-label="Silhouette meditating before misty mountains" style="background:radial-gradient(circle at 50% 20%,#fff6d0,#9fb8a0 45%,#2f7c80 80%)"></div>
    <p class="event-name">An evening with<br>Elias Marwood in CA</p>
    <p class="event-date">September 19, 2022</p>
  </article>
  <article class="event-card" style="left:399px">
    <div class="event-photo" role="img" aria-label="Stacked stones among autumn leaves" style="background:radial-gradient(circle at 55% 40%,#f3d36a,#c99630 55%,#6b5a25 100%)"></div>
    <p class="event-name">An evening with<br>Elias Marwood in CA</p>
    <p class="event-date">September 19, 2022</p>
  </article>
  <article class="event-card" style="left:570px;top:158px">
    <div class="event-photo" role="img" aria-label="Person with raised arms facing an autumn hillside" style="background:radial-gradient(circle at 50% 30%,#c9c9c4,#8a7456 55%,#3b2f33 100%)"></div>
    <p class="event-name">An evening with<br>Elias Marwood in CA</p>
    <p class="event-date">September 19, 2022</p>
  </article>
  <article class="event-card" style="left:740px;top:158px">
    <div class="event-photo" role="img" aria-label="Meditating silhouette with a glowing light against a starry galaxy" style="background:radial-gradient(circle at 50% 55%,#f7c060,#8a5a55 30%,#2a3a66 65%,#15203e 100%)"></div>
    <p class="event-name">An evening with<br>Elias Marwood in CA</p>
    <p class="event-date">September 19, 2022</p>
  </article>
  <div class="btn-events">View all events</div>
</section>
<div class="events-band"></div>

<footer class="site-footer">
  <div class="contact">Email: support@harmoniaway.com<br>Phone: 012-555-0148</div>
  <div class="divider" style="left:446px"></div>
  <div class="social" aria-label="Social links"><span></span><span></span><span></span><span></span></div>
  <div class="divider" style="left:674px"></div>
  <div class="legal">Copyright © 2022 HarmoniaWay.com<br>All rights reserved.</div>
</footer>
</body>
</html>
```